Bakery and cafe
Savor Every Crumb Now
Project: Bakery and cafe
Bakery and cafe -
Creative Brief
Use specific fonts
Classy, elegant, close to logo font
Bright & Fun-filled
Harlowe
Owner
1785 Brookvale dr Atlanta, Ga. 30318
jmharlowe@hqbakeryandcafe.example
www.hqbakeryandcafe.example
want both vertical and horizontal draft. Really want a vertical card.
Logo in black and white. or gray scale depending on the color of the front and the actual card.

```html
<!DOCTYPE html>
<html lang="en">
<head>
<meta charset="utf-8">
<title>HQ Bakery &amp; Cafe – Stationery</title>
<link rel="stylesheet" href="https://fonts.googleapis.com/css2?family=Playfair+Display:wght@700&family=Great+Vibes&family=Open+Sans:wght@400;600&display=swap">
<style>
  :root{
    --brown:#7b2d1d;
    --red:#d42a1f;
    --orange:#ec6a2a;
    --ink:#7b2d1d;
    --faint:#efe4de;
    --paper:#ffffff;
    --bg:#ffffff;
    --edge:#d9d9d9;
  }
  *{margin:0;padding:0;box-sizing:border-box}
  html,body{width:1200px;height:1037px;overflow:hidden;background:var(--bg)}
  body{position:relative;font-family:"Open Sans",Arial,sans-serif;color:var(--ink)}
  .sheet{position:absolute;background:var(--paper);border:1px solid var(--edge);overflow:hidden;box-shadow:0 1px 3px rgba(0,0,0,.12)}
  .sheet svg.wave{position:absolute;left:0;bottom:0;width:100%}
  .brand{position:absolute;text-align:center}
  .brand-mark{display:block;margin:0 auto;border-radius:50%;background:var(--red)}
  .brand-name{font-family:"Playfair Display",Georgia,serif;font-weight:700;color:var(--brown);white-space:nowrap;display:block;line-height:1.2}
  .brand-tagline{font-family:"Great Vibes",cursive;color:var(--orange);white-space:nowrap;display:block;line-height:1.1}
  .faint-mark{position:absolute;border-radius:50%;background:var(--faint)}
  .contact{position:absolute;color:#fff;line-height:1.5;white-space:nowrap}

  .letterhead{left:63px;top:63px;width:731px;height:943px}
  .letterhead .brand{left:40px;top:40px}
  .letterhead .brand-mark{width:26px;height:26px;margin-bottom:8px}
  .letterhead .brand-name{font-size:18px}
  .letterhead .brand-tagline{font-size:16px}
  .letterhead .faint-mark{left:400px;top:530px;width:230px;height:230px}
  .letterhead .contact{left:36px;bottom:18px;font-size:13px}

  .envelope{left:323px;top:94px;width:820px;height:357px}
  .envelope .brand{left:24px;top:26px}
  .envelope .brand-mark{width:22px;height:22px;margin-bottom:6px}
  .envelope .brand-name{font-size:18px}
  .envelope .brand-tagline{font-size:15px}
  .envelope .faint-mark{left:672px;top:150px;width:120px;height:120px}
  .envelope .contact{left:24px;bottom:14px;font-size:12px}

  .card-front{left:814px;top:586px;width:100px;height:228px}
  .card-front .brand{left:0;top:14px;width:100px}
  .card-front .brand-mark{width:12px;height:12px;margin-bottom:4px}
  .card-front .brand-name{font-size:8px}
  .card-front .brand-tagline{font-size:7.5px}
  .card-front .holder{position:absolute;left:0;top:92px;width:100px;text-align:center;color:var(--brown)}
  .card-front .holder-name{font-size:10px;font-weight:600}
  .card-front .holder-role{font-size:7px;color:var(--orange)}
  .card-front .contact{left:7px;font-size:4.6px}
  .card-front .contact.address{top:148px}
  .card-front .contact.online{top:196px}

  .card-back{left:931px;top:586px;width:98px;height:228px;background:var(--brown)}
  .card-back .faint-mark{left:6px;top:100px;width:70px;height:70px;background:var(--orange);opacity:.55}
  .card-back .site{position:absolute;left:82px;top:10px;color:#fff;font-size:7px;writing-mode:vertical-rl;white-space:nowrap}
</style>
</head>
<body>

<section class="sheet letterhead">
  <div class="brand">
    <span class="brand-mark"></span>
    <span class="brand-name">HQ BAKERY &amp; CAFE</span>
    <span class="brand-tagline">Savor Every Crumb Now</span>
  </div>
  <div class="faint-mark"></div>
  <svg class="wave" viewBox="0 0 731 160" height="160" preserveAspectRatio="none">
    <path d="M0 40 Q300 -10 731 10 L731 160 L0 160Z" fill="var(--orange)"/>
    <path d="M0 52 Q300 2 731 20 L731 160 L0 160Z" fill="var(--red)"/>
    <path d="M0 64 Q300 16 731 34 L731 160 L0 160Z" fill="var(--brown)"/>
  </svg>
  <div class="contact">
    1785 Brookvale dr Atlanta, Ga. 30318<br>
    Cell : 404-555-0182<br>
    www.hqbakeryandcafe.example
  </div>
</section>

<section class="sheet envelope">
  <div class="brand">
    <span class="brand-mark"></span>
    <span class="brand-name">HQ BAKERY &amp; CAFE</span>
    <span class="brand-tagline">Savor Every Crumb Now</span>
  </div>
  <div class="faint-mark"></div>
  <svg class="wave" viewBox="0 0 820 100" height="100" preserveAspectRatio="none">
    <path d="M0 40 Q400 -6 820 6 L820 100 L0 100Z" fill="var(--orange)"/>
    <path d="M0 50 Q400 4 820 16 L820 100 L0 100Z" fill="var(--red)"/>
    <path d="M0 60 Q400 16 820 28 L820 100 L0 100Z" fill="var(--brown)"/>
  </svg>
  <div class="contact">1785 Brookvale dr Atlanta, Ga. 30318</div>
</section>

<section class="sheet card-front">
  <div class="brand">
    <span class="brand-mark"></span>
    <span class="brand-name">HQ BAKERY &amp; CAFE</span>
    <span class="brand-tagline">Savor Every Crumb Now</span>
  </div>
  <div class="holder">
    <div class="holder-name">Harlowe</div>
    <div class="holder-role">Owner</div>
  </div>
  <svg class="wave" viewBox="0 0 100 100" height="100" preserveAspectRatio="none">
    <path d="M0 22 Q50 0 100 4 L100 100 L0 100Z" fill="var(--orange)"/>
    <path d="M0 26 Q50 4 100 8 L100 100 L0 100Z" fill="var(--red)"/>
    <path d="M0 30 Q50 9 100 13 L100 100 L0 100Z" fill="var(--brown)"/>
  </svg>
  <div class="contact address">1785 Brookvale dr<br>Atlanta, Ga. 30318<br>Cell : 404-555-0182</div>
  <div class="contact online">jmharlowe@hqbakeryandcafe.example<br>www.hqbakeryandcafe.example</div>
</section>

<section class="sheet card-back">
  <div class="faint-mark"></div>
  <div class="site">www.hqbakeryandcafe.example</div>
</section>

</body>
</html>
```